Vitamin gum packaging artwork

Artwork and branding for Brellox Ltd.'s Chewloria. Artwork should be transferable for use on blister packaging, plastic tub, or box packaging format, see pictures. Innovative packaging design ideas are also welcome. Think Glintsplash, trendy consumer good targeting 24-48 yr olds. Supermarket, convenience store, impulse purchase product NOT strictly pharmaceutical retail. Design concept should also lend itself to necessary colour/graphic changes for flavours of 'Fresh Spearmint' and 'Cool Peppermint'. Key text to include: Product name: Chewloria, Flavour, Multivitamin chewing gum, Formulated by Medical Doctors, chew two, one serving (2 pieces) provides 100% of an adults daily requirement of vitamins and minerals, nutritional supplement.

Industry/Entity Type

Plastic

```html
<!DOCTYPE html>
<html lang="en">
<head>
<meta charset="utf-8">
<title>Chewloria Multivitamin Chewing Gum – Label Artwork</title>
<link rel="stylesheet" href="https://fonts.googleapis.com/css2?family=Open+Sans:ital,wght@0,400;0,600;0,700;0,800;1,700&display=swap">
<style>
  :root {
    --canvas-top: #ffffff;
    --canvas-bottom: #dcdcdc;
    --ink: #111111;
    --ink-grey: #555555;
    --white: #ffffff;
    --spearmint: #6cbf3a;
    --spearmint-deep: #58a82c;
    --spearmint-leaf: #3f8f2a;
    --peppermint: #1f63b8;
    --peppermint-deep: #0e4f9f;
    --peppermint-leaf: #4a9a3a;
    --gum-white: #eef5fb;
  }
  * { box-sizing: border-box; margin: 0; padding: 0; }
  html, body { width: 1200px; height: 1000px; overflow: hidden; }
  body {
    position: relative;
    background: radial-gradient(ellipse at 50% 40%, var(--canvas-top) 30%, var(--canvas-bottom) 100%);
    font-family: "Open Sans", Arial, sans-serif;
  }
  .label-row {
    position: absolute;
    top: 285px;
    left: 28px;
    display: flex;
    gap: 20px;
  }
  .label {
    position: relative;
    width: 562px;
    height: 450px;
    background: linear-gradient(90deg, var(--white) 0%, var(--white) 47%, var(--flavour) 75%, var(--flavour-deep) 100%);
    overflow: hidden;
  }
  .label--spearmint { --flavour: var(--spearmint); --flavour-deep: var(--spearmint-deep); --leaf: var(--spearmint-leaf); }
  .label--peppermint { --flavour: var(--peppermint); --flavour-deep: var(--peppermint-deep); --leaf: var(--peppermint-leaf); }
  .label--peppermint { width: 556px; }

  .company-tab {
    position: absolute;
    left: 30px;
    top: 0;
    width: 172px;
    height: 47px;
    background: var(--ink);
    border-radius: 0 0 12px 12px;
    color: var(--white);
    font-weight: 800;
    font-size: 19px;
    line-height: 47px;
    text-align: center;
    padding-top: 2px;
  }
  .company-claim {
    position: absolute;
    left: 39px;
    top: 51px;
    font-size: 11px;
    color: var(--ink);
  }
  .sub-brand {
    position: absolute;
    left: 64px;
    top: 104px;
    font-size: 27px;
    font-weight: 700;
    color: var(--flavour);
    letter-spacing: -0.5px;
  }
  .product-name {
    position: absolute;
    left: 62px;
    top: 124px;
    font-size: 84px;
    font-weight: 700;
    color: var(--ink);
    letter-spacing: -3px;
    line-height: 1.1;
  }
  .leaf {
    position: absolute;
    left: 22px;
    top: 222px;
    width: 80px;
    height: 64px;
    border-radius: 60% 40% 55% 45%;
    background: radial-gradient(circle at 40% 40%, #8fd468, var(--leaf));
  }
  .flavour {
    position: absolute;
    left: 78px;
    top: 226px;
    font-size: 26px;
    font-weight: 700;
    font-style: italic;
    color: var(--ink);
  }
  .flavour strong {
    color: var(--flavour);
    font-weight: 800;
    text-transform: uppercase;
    letter-spacing: 0.5px;
  }
  .descriptor {
    position: absolute;
    left: 31px;
    top: 296px;
    color: var(--ink-grey);
  }
  .descriptor h2 { font-size: 18px; font-weight: 700; line-height: 1.25; }
  .descriptor p { font-size: 14px; line-height: 1.3; }
  .gum-pieces {
    position: absolute;
    left: 18px;
    top: 372px;
    width: 96px;
    height: 70px;
    border-radius: 50%;
    background: radial-gradient(circle at 50% 50%, var(--gum-white) 35%, var(--flavour) 100%);
  }
  .serving {
    position: absolute;
    left: 128px;
    top: 382px;
    font-size: 11.5px;
    line-height: 1.35;
    color: var(--ink);
  }
</style>
</head>
<body>
  <main class="label-row">
    <article class="label label--spearmint">
      <div class="company-tab">Brellox Ltd</div>
      <p class="company-claim">Formulated by Medical Doctors</p>
      <p class="sub-brand">Brellox</p>
      <h1 class="product-name">Chewloria</h1>
      <div class="leaf" role="img" aria-label="Fresh spearmint leaf illustration"></div>
      <p class="flavour">fresh <strong>Spearmint</strong></p>
      <div class="descriptor">
        <h2>Multivitamin Chewing Gum</h2>
        <p>Sugar Free. Aspartame Free.<br>Naturally sweetened. Naturally Flavoured</p>
      </div>
      <div class="gum-pieces" role="img" aria-label="Two white gum pellets on a green halftone dot"></div>
      <p class="serving">2 pieces = 100% Adults<br>Vitamin &amp; Mineral<br>requirements</p>
    </article>

    <article class="label label--peppermint">
      <div class="company-tab">Brellox Ltd</div>
      <p class="company-claim">Formulated by Medical Doctors</p>
      <p class="sub-brand">Brellox</p>
      <h1 class="product-name">Chewloria</h1>
      <div class="leaf" role="img" aria-label="Cool peppermint sprig illustration"></div>
      <p class="flavour">cool <strong>Peppermint</strong></p>
      <div class="descriptor">
        <h2>Multivitamin Chewing Gum</h2>
        <p>Sugar Free. Aspartame Free.<br>Naturally sweetened. Naturally Flavoured</p>
      </div>
      <div class="gum-pieces" role="img" aria-label="Two white gum pellets on a blue halftone dot"></div>
      <p class="serving">2 pieces = 100% Adults<br>Vitamin &amp; Mineral<br>requirements</p>
    </article>
  </main>
</body>
</html>
```